Norvane Builders Business Card

Modern and Professional Business Card for a Med size construction/development company.

See the samples below for the design I like … but I need ideas for incorporating the red company logo while still keeping the clean look of the card samples that are attached.

Logo and tag line on the back … info on the front.

Tagline: Quality Starts from the Ground Up

Target Market(s)

Med-Large General Contractors

Contact Information for Business Card

Norvane Builders Limited
42 Brenton Street
Elk Harbour, NL
B3K 7T2

t: 709-555-0147
f: 709-555-0192
w: www.norvanebuilders-example.com

Font styles to use
Sans Serif

Colors
fbee3e

Requirements
Must have
• I like the black and yellow designs of the attached samples …. but I'm not sure how to incorporate the red Norvane Builders logo into that design??
Nice to have
• Construction safety strips

```html
<!DOCTYPE html>
<html lang="en">
<head>
<meta charset="utf-8">
<title>Norvane Builders Business Card</title>
<link rel="stylesheet" href="https://fonts.googleapis.com/css2?family=Lato:wght@400;700;900&display=swap">
<style>
  :root {
    --yellow: #f8ee46;
    --red: #e0161e;
    --ink: #4a4a4a;
    --black: #1b1b1b;
    --white: #ffffff;
    --stage: #e9e7e2;
  }
  * { margin: 0; padding: 0; box-sizing: border-box; }
  html, body { width: 1200px; height: 1200px; overflow: hidden; background: var(--stage); }
  body { position: relative; font-family: "Lato", Arial, sans-serif; }
  .card {
    position: absolute; left: 150px; width: 900px; height: 525px;
    border-radius: 24px; overflow: hidden; background: var(--yellow);
    box-shadow: 0 6px 14px rgba(0,0,0,0.25);
  }
  .card--front { top: 55px; }
  .card--back { top: 620px; }
  .front-shape { position: absolute; inset: 0; }
  .contact { position: absolute; left: 40px; top: 70px; color: var(--ink); }
  .contact__name { color: var(--red); font-weight: 700; font-size: 36px; line-height: 1.1; }
  .contact__role { font-size: 26px; line-height: 1.3; font-weight: 700; color: var(--ink); }
  .contact__lines { list-style: none; margin-top: 42px; }
  .contact__lines li { display: flex; align-items: center; gap: 6px; font-size: 26px; line-height: 32px; }
  .contact__lines svg { width: 28px; height: 26px; flex: none; }
  .company { margin-top: 54px; font-size: 26px; line-height: 32px; }
  .company__name { color: var(--red); font-weight: 700; }
  .brand-mark {
    position: absolute; left: 588px; top: 240px; width: 290px; text-align: center;
    color: var(--red); font-weight: 900; font-size: 34px; line-height: 1;
  }
  .back-brand {
    position: absolute; left: 0; right: 0; top: 180px; text-align: center;
    color: var(--black); font-weight: 900; font-size: 62px; line-height: 1;
  }
  .tagline {
    position: absolute; left: 0; right: 0; top: 335px; text-align: center;
    color: var(--red); font-weight: 700; font-size: 36px; line-height: 1;
  }
</style>
</head>
<body>
  <section class="card card--front">
    <svg class="front-shape" viewBox="0 0 900 525" width="900" height="525" aria-hidden="true">
      <path d="M538 0 Q440 262 571 525 L900 525 L900 0 Z" fill="var(--black)"/>
      <path d="M571 0 Q460 262 571 525 L900 525 L900 0 Z" fill="var(--white)"/>
    </svg>
    <div class="contact">
      <h1 class="contact__name">Dara Keller</h1>
      <p class="contact__role">Civil Engineer</p>
      <ul class="contact__lines">
        <li>
          <svg viewBox="0 0 24 24"><path d="M6.6 3.5 9 6.2 7.6 8.7c1 2.2 2.6 3.9 4.8 5l2.5-1.4 2.7 2.4-1.5 3.2C10 17.7 5.7 13.4 3.4 6.5Z" fill="none" stroke="var(--red)" stroke-width="2" stroke-linejoin="round"/><path d="M14 3a7 7 0 0 1 7 7M14 7a3 3 0 0 1 3 3" fill="none" stroke="var(--red)" stroke-width="2"/></svg>
          <span>709-555-0147</span>
        </li>
        <li>
          <svg viewBox="0 0 24 24"><rect x="7" y="3" width="10" height="6" fill="none" stroke="var(--red)" stroke-width="2"/><rect x="3" y="9" width="18" height="8" rx="1.5" fill="none" stroke="var(--red)" stroke-width="2"/><rect x="7" y="14" width="10" height="7" fill="var(--yellow)" stroke="var(--red)" stroke-width="2"/></svg>
          <span>709-555-0192</span>
        </li>
        <li>
          <svg viewBox="0 0 24 24"><rect x="2" y="4" width="20" height="13" rx="1.5" fill="none" stroke="var(--red)" stroke-width="2"/><path d="M9 21h6M12 17v4" stroke="var(--red)" stroke-width="2"/><circle cx="12" cy="10.5" r="3" fill="none" stroke="var(--red)" stroke-width="1.5"/></svg>
          <span>www.norvanebuilders-example.com</span>
        </li>
      </ul>
      <address class="company" style="font-style:normal">
        <div class="company__name">Norvane Builders Limited</div>
        <div>42 Brenton Street</div>
        <div>Elk Harbour, NL, B3K 7T2</div>
      </address>
    </div>
    <div class="brand-mark">Norvane Builders</div>
  </section>

  <section class="card card--back">
    <div class="back-brand">Norvane Builders</div>
    <p class="tagline">Quality Starts From The Ground Up</p>
  </section>
</body>
</html>
```